Need Business Cards for my Business

email address: rkpmarlowhollowworks@vendrimail.com
web address: rkpmarlowhollowworks.net
Slogan: We offer various QVN licenses
Rowland K. Pemberly
Please stick with colors of Company Logo
would like the card to be more of the color example of the logo.
If you need PDF copy of logo email me at the above account.
Creative control rests with you.

Industry/Entity Type

Business

Contact Information for Business Card

I am a minimalist, but would like something to pop and stand out amongst other cards, make it memorable.

Font styles to use
Serif
Decorative
Script

```html
<!DOCTYPE html>
<html lang="en">
<head>
<meta charset="utf-8">
<title>Marlow Hollow Works – Business Card</title>
<link rel="stylesheet" href="https://fonts.googleapis.com/css2?family=Roboto:wght@300;400;700&display=swap">
<style>
  :root {
    --ink: #1e1c1c;
    --paper: #ffffff;
    --stage: #e4e2df;
    --muted: #3a3838;
  }
  * { margin: 0; padding: 0; box-sizing: border-box; }
  html, body {
    width: 1200px; height: 892px; overflow: hidden;
    background: var(--stage);
    font-family: "Roboto", Arial, sans-serif;
    color: var(--ink);
  }
  .sheet {
    width: 1200px; height: 892px;
    display: flex; flex-direction: column;
    align-items: center; justify-content: center; gap: 48px;
  }
  .card {
    position: relative;
    width: 630px; height: 360px;
    background: var(--paper);
    box-shadow: 0 6px 18px rgba(0,0,0,.18);
    overflow: hidden;
  }

  /* ---------- front ---------- */
  .front .brand {
    position: absolute; top: 40px; right: 44px;
    display: flex; align-items: center; gap: 14px;
  }
  .brand-dot {
    width: 30px; height: 30px; border-radius: 50%;
    background: var(--ink);
  }
  .brand-name {
    font-weight: 700; font-size: 34px; letter-spacing: 1px;
    text-transform: uppercase; color: var(--ink);
  }
  .front .slogan {
    position: absolute; top: 104px; right: 44px;
    font-weight: 400; font-size: 15px; letter-spacing: 4.5px;
    color: var(--muted);
  }
  .front .rule-top {
    position: absolute; left: 0; right: 0; top: 150px;
    height: 2px; background: var(--ink);
  }
  .front .band {
    position: absolute; left: 0; right: 0; top: 158px; height: 176px;
    background: var(--ink); color: var(--paper);
    display: flex; align-items: stretch;
  }
  .front .rule-bottom {
    position: absolute; left: 0; right: 0; top: 340px;
    height: 2px; background: var(--ink);
  }
  .holder {
    flex: 0 0 300px; padding: 28px 0 0 34px;
    font-weight: 400; font-size: 20px;
  }
  .divider {
    width: 1px; background: var(--paper); margin: 70px 0 18px;
  }
  .contacts {
    list-style: none; padding: 74px 0 0 22px;
    display: flex; flex-direction: column; gap: 10px;
    font-size: 14px; font-weight: 300;
  }
  .contacts li { display: flex; align-items: center; gap: 10px; }
  .contacts .icon {
    width: 18px; height: 18px; background: var(--paper);
    display: flex; align-items: center; justify-content: center; flex: none;
  }

  /* ---------- back ---------- */
  .back .rule {
    position: absolute; left: 0; right: 0; height: 3px; background: var(--ink);
  }
  .back .rule.upper { top: 100px; }
  .back .rule.lower { top: 257px; }
  .back .band {
    position: absolute; left: 0; right: 0; top: 110px; height: 140px;
    background: var(--ink);
    display: flex; align-items: center; justify-content: center; gap: 18px;
  }
  .back .brand-dot { background: var(--paper); width: 40px; height: 40px; }
  .back .brand-name { color: var(--paper); font-size: 40px; }
</style>
</head>
<body>
<main class="sheet">

  <section class="card front" aria-label="Business card front">
    <div class="brand">
      <span class="brand-dot"></span>
      <span class="brand-name">Marlow Hollow Works</span>
    </div>
    <p class="slogan">We offer various QVN licenses</p>
    <div class="rule-top"></div>
    <div class="band">
      <p class="holder">Rowland K. Pemberly</p>
      <div class="divider"></div>
      <ul class="contacts">
        <li>
          <span class="icon">
            <svg width="12" height="12" viewBox="0 0 12 12"><path d="M2.5 1h2l1 2.5-1.3 1a6 6 0 0 0 3.3 3.3l1-1.3L11 7.5v2A1.5 1.5 0 0 1 9.5 11 8.5 8.5 0 0 1 1 2.5 1.5 1.5 0 0 1 2.5 1z" fill="#1e1c1c"/></svg>
          </span>555-204-7316
        </li>
        <li>
          <span class="icon">
            <svg width="12" height="12" viewBox="0 0 12 12" fill="none" stroke="#1e1c1c" stroke-width="1"><circle cx="6" cy="6" r="5"/><ellipse cx="6" cy="6" rx="2.2" ry="5"/><path d="M1 6h10M2 3.3h8M2 8.7h8"/></svg>
          </span>rkpmarlowhollowworks.net
        </li>
        <li>
          <span class="icon">
            <svg width="12" height="10" viewBox="0 0 12 10" fill="none" stroke="#1e1c1c" stroke-width="1.2"><rect x="0.6" y="0.6" width="10.8" height="8.8"/><path d="M0.6 0.6 6 5.5l5.4-4.9"/></svg>
          </span>rkpmarlowhollowworks@vendrimail.com
        </li>
      </ul>
    </div>
    <div class="rule-bottom"></div>
  </section>

  <section class="card back" aria-label="Business card back">
    <div class="rule upper"></div>
    <div class="band">
      <span class="brand-dot"></span>
      <span class="brand-name">Marlow Hollow Works</span>
    </div>
    <div class="rule lower"></div>
  </section>

</main>
</body>
</html>
```